依頼詳細
・表面のみ

・内容は同デザインで2サイズ(角2と長3)

・封筒の色は水色(アクア)
下記ペーパリオの既成封筒のアクアです
https://www.paperio-shiki.jp/items/futo/std_ready
(長3は郵便番号枠が印字されています)

・文字色は黒(墨)、字体はお任せします。

・原稿はワードデータあり

・文字の位置は添付データの内容が希望ですが、わかりやすくデザインしていただいてかまいません。

記載項目
ミナセカワ草花健康株式会社
〒408-2703 山梨県北杜市大泉町東原字柳沢6157-304
TEL : 0551-82-3916   FAX : 0551-82-3919
Minasekawa  ペンタゴンボタニカル草木探究
(八ヶ岳・浅間山・富士山・箱根)

希望イメージ
シンプル 複雑
単色 カラフル
暗い 明るい
日常 高級
遊び心 厳粛
未来的 伝統的
女性的 男性的
希望する色
青系
納品ファイル
• イラストレーター形式 (.ai)
補足説明
納品ファイル:担当がイラストレーターが見えないので、PDFデータで内容の確認を行い、最終納品時はイラストレーターデータでお願いします。
当選後、1~2回の修正があると思います。
■ 選んだ理由

スッキリと見やすく、ハーブを扱う弊社のイメージが伝わりやすいと思い選ばせていただきました。
「MINASEKAWA ペンタゴンボタニカル草木探究」のデザイン部分が気に入りました。

■ 提案者全員のお礼・コメント

この度は、たくさんのご応募ありがとうございました。
素敵なデザインばかりで選定するのに迷いました。
また、募集させていただくことがあると思いますので、
その際はよろしくお願いいたします。

```html
<!DOCTYPE html>
<html lang="ja">
<head>
<meta charset="utf-8">
<title>ミナセカワ草花健康株式会社 長3封筒</title>
<link rel="stylesheet" href="https://fonts.googleapis.com/css2?family=Noto+Sans+JP:wght@400;500;700&family=Noto+Serif+JP:wght@500&display=swap">
<style>
  :root {
    --backdrop: #ececec;
    --envelope: #c9e3f2;
    --envelope-edge: #b7d3e4;
    --ink: #1a1a1a;
    --herb-fill: #bcd6e6;
  }
  * { margin: 0; padding: 0; box-sizing: border-box; }
  html, body { width: 1200px; height: 2420px; overflow: hidden; background: var(--backdrop); }
  .canvas { position: relative; width: 1200px; height: 2420px; font-family: "Noto Sans JP", sans-serif; color: var(--ink); }
  .envelope-shape { position: absolute; inset: 0; }
  .herb-illustration {
    position: absolute; left: 470px; top: 1580px; width: 260px; height: 300px;
    background: var(--herb-fill); border-radius: 40% 40% 20% 20%;
  }
  .company-name {
    position: absolute; left: 0; width: 1200px; top: 1935px; text-align: center;
    font-family: "Noto Serif JP", serif; font-weight: 500; font-size: 56px; letter-spacing: 2px;
  }
  .address { position: absolute; left: 192px; top: 2046px; font-size: 26px; letter-spacing: 1px; }
  .contact { position: absolute; top: 2096px; display: flex; align-items: center; gap: 12px; font-size: 40px; }
  .contact.tel { left: 192px; }
  .contact.fax { left: 600px; }
  .contact .label {
    border: 2px solid var(--ink); font-size: 24px; line-height: 1; padding: 4px 6px; letter-spacing: 1px;
  }
  .brand-box {
    position: absolute; left: 192px; top: 2200px; width: 304px; height: 96px;
    border: 2px solid var(--ink); border-radius: 10px;
    display: flex; align-items: center; justify-content: center;
    font-family: "Noto Serif JP", serif; font-size: 40px; letter-spacing: 2px;
  }
  .research { position: absolute; left: 530px; top: 2196px; text-align: center; }
  .research .title { font-weight: 700; font-size: 40px; letter-spacing: 1px; }
  .research .regions { font-size: 26px; margin-top: 6px; letter-spacing: 1px; }
</style>
</head>
<body>
<div class="canvas">
  <svg class="envelope-shape" width="1200" height="2420" viewBox="0 0 1200 2420">
    <defs>
      <filter id="soft-shadow" x="-5%" y="-5%" width="110%" height="110%">
        <feDropShadow dx="0" dy="4" stdDeviation="6" flood-opacity="0.18"/>
      </filter>
    </defs>
    <g filter="url(#soft-shadow)">
      <polygon points="104,34 1096,34 1112,160 88,160" fill="var(--envelope)"/>
      <rect x="88" y="158" width="1024" height="2182" fill="var(--envelope)"/>
    </g>
    <line x1="88" y1="160" x2="1112" y2="160" stroke="var(--envelope-edge)" stroke-width="2"/>
  </svg>

  <div class="herb-illustration" role="img" aria-label="ハーブの線画イラスト"></div>

  <div class="company-name">ミナセカワ草花健康株式会社</div>
  <div class="address">〒408-2703　山梨県北杜市大泉町東原字柳沢6157-304</div>
  <div class="contact tel"><span class="label">TEL</span><span>0551-82-3916</span></div>
  <div class="contact fax"><span class="label">FAX</span><span>0551-82-3919</span></div>

  <div class="brand-box">Minasekawa</div>
  <div class="research">
    <div class="title">ペンタゴンボタニカル草木探究</div>
    <div class="regions">（八ヶ岳・浅間山・富士山・箱根）</div>
  </div>
</div>
</body>
</html>
```